Revolutionary Video Platform (uncoded) - updated 05.11.

We want you to design the frontpage (uncoded) of FLIRTNOVA.net (we ev. hire the winner to create the subpages).

The concept of FLIRTNOVA.net is to show (ONLY!) infield videos of dating coaches (when they get in contact with women on the street) so that the users will have a solid base for deciding which coach they want to contact. I highlight that because some designs contained other ideas like "dating tips". No, we are specialized on infield videos. People should see if these coaches are really worth their money.

Therefore, the frontpage must include the following:

Header: Logo (attached), writing "FLIRTNOVA" or "FLIRT NOVA", links "Contact", "About", "Sign In", "Sign Up"

No design yet tried to change the logo in its size. You're welcome to do creative stuff.

What else is necessary on the front page:

1. 2 statements:

"Because 34 videos prove how to get every woman you want."
"Connect directly with 26 dating-coaches from these videos!"

The numbers should be showed in a way that the users know that they count up automatically; important: use the style zemlo has on it's front page by showing their amount of users.

2. Top rated Dating Coaches:

As the videos on the site can be rated, we want the coaches with the best rated videos on the front page with their faces (people can jump from there directly to their profiles).

To the pictures of the coaches you should also add the country flag and the city (where they come from). Plus, users should see who's on the first place, who's on the second place.. max. 10 coaches on the front page..

Set the title "TOP 10 DATING COACHES listed by best rated videos"

3. Search System

In order to find the videos the user is searching for, it needs a simple search form, where they can search after:

- Language
- Country
- City
- Rating
- Level of Difficulty
- Set-Size
- Conversation Starter

You can use simple white bars with a drop-down button.

4. Tags

Implement tags like "bitch shield, blow out opener, bounce, calibration, canned routine, challenge point, cockblock, cold approach, cold reading, compliment opener" etc.

Alphabetically listed..

5. Create previews of the (searched) videos which contains:

- Thumbnail of the video (only thumbnails on front page, no bigger video playback window, pls use pictures in order to make the site look more real)

- Some infos about the video (name of the coach with user-picture, duration, language, country (name and flag), city, audio comment (yes/no), difficulty level (super easy-expert), views, points needed to view (1-3), 5 star rating)

- Title and the beginning of the text about the video (written by the coach), i.e. about 30 words

- There are 2 sorts of videos.. (it's not necessary to explain why, it's just important that you implement two different versions of the video preview area (different only in terms of color!).. for example, some video preview areas could be edged in gold, others in silver.. or you could fill the whole video preview area with a color.. show me your taste... even though I prefer the more elegant way like gold and silver, you can probably surprise me with other color combinations..

- In order to simplify the process of comparing your designs, pls create 4 such preview video are areas..

6. Best voted video reviewer:

Users AND coaches will be able to write reviews about the videos. These reviews can be liked/voted. Therefore, we will know which user or coach writes the best reviews.

So we want you to implement also the charts of the 10 best voted video reviewers. Make sure there is a ranking list with the name of the user/coach and how many likes he got.
Here as well: add country flag, country and city (to see where they come from)..plus a little thumbnail of the profile picture.. Make sure the best 3 are being highlighted somehow..
Updates

Some designs were quite creative so far.
But unfortunately, less than half of the designers considered all requirements.
Therefore, be sure to implement all the requirements (for example, check new point nr. 6).
Without considering all the requirements, you don't have a chance to win this content.

Thank you.

Target Market(s)

male, 16-40 years old, worldwide audience

Industry/Entity Type

Dating

Requirements
Must have
• Not all submitted designs considered all requirements.

Therefore, please read the requirements carefully and consider all of them. If you want to add some new ideas or if you decide not to implement some requirements, I suggest to submit a second design.
Nice to have
• - if you have other ideas, feel free to add some of them to the front page, probably in form of a second design

- sometimes the same page will look totally different in other colors. Therefore, it would be great to add a 2nd version of your design, in terms of color

- the front page needs to be an eye-catcher

- different FLIRTNOVA font styles (come up with your own taste), a few different styles would be great!
Should not have
• - a search field like there is one in the first submitted design (the intelligent search is already being available with the filter system and the tags)

- female colors like pink/purple (it's a site only for men)

- a 08/15 look.. this will be the first website worldwide which contains videos from the best dating gurus on this planet in action.. they deserve a cool place to show their videos in order to gain new customers..

```html
<!DOCTYPE html>
<html lang="en">
<head>
<meta charset="utf-8">
<title>FLIRT NOVA – Dating Coach Videos</title>
<link href="https://fonts.googleapis.com/css2?family=Open+Sans:ital,wght@0,400;0,600;0,700;1,700&family=Arimo:wght@400;700&display=swap" rel="stylesheet">
<style>
:root{
  --orange:#d9530f;
  --orange-light:#f07a35;
  --ink:#444;
  --tag:#c4c0bf;
  --tag-strong:#4a4a4a;
  --page:#efebea;
  --dark:#232021;
  --gold:#f2c11d;
  --gold-dark:#d9a50c;
  --yellow:#f6c624;
}
*{box-sizing:border-box;margin:0;padding:0}
html,body{width:1198px;height:1200px;overflow:hidden}
body{font-family:"Arimo",Arial,sans-serif;color:var(--ink);background:var(--page)}
.page{position:relative;width:1198px;height:1200px;background:linear-gradient(#f6f4f4 0,#efebea 600px,#ebe7e6 1150px)}
.header-band{position:absolute;left:0;top:0;width:1198px;height:168px;background:linear-gradient(#fdfdfd 0,#f0efef 60%,#d9d7d7 100%);border-bottom:1px solid #cfcdcd;box-shadow:0 3px 5px rgba(0,0,0,.12)}
.mascot{position:absolute;left:178px;top:8px;width:82px;height:90px;background:linear-gradient(#3a3a3a,#1b1b1b);border-radius:40px 40px 6px 6px;opacity:.85}
.brand{position:absolute;left:150px;top:106px;font-family:"Open Sans",sans-serif;font-weight:700;font-size:24px;color:var(--orange);letter-spacing:.5px}
.bubble{position:absolute;background:#fff;border-radius:50%;box-shadow:0 4px 10px rgba(0,0,0,.06)}
.bubble--videos{left:398px;top:-18px;width:278px;height:122px}
.bubble--coaches{left:800px;top:-18px;width:250px;height:124px}
.counter{position:absolute;border-radius:50%;background:#353535;color:var(--yellow);font-family:"Open Sans",sans-serif;display:flex;align-items:center;justify-content:center;border:2px solid #fff}
.counter--videos{left:340px;top:15px;width:72px;height:72px;font-size:40px}
.counter--coaches{left:986px;top:2px;width:60px;height:52px;font-size:30px}
.statement{position:absolute;font-family:"Open Sans",sans-serif;font-weight:600;font-size:15px;line-height:23px;color:#222;letter-spacing:.8px}
.statement--videos{left:416px;top:28px}
.statement--coaches{left:808px;top:24px;line-height:21px;text-align:center}
.nav{position:absolute;left:150px;top:145px;width:898px;height:38px;background:linear-gradient(var(--orange-light),var(--orange) 60%,#c9480a);border-radius:6px 6px 0 0;display:flex}
.nav a{display:block;height:38px;line-height:36px;color:#fff;font-size:12px;letter-spacing:1px;text-decoration:none;padding:0 32px 0 42px;border-right:1px solid #b84308}
.nav a:first-child{padding-left:43px}
.nav a:nth-child(5){border:none}
.hero{position:absolute;left:150px;top:182px;width:898px;height:386px;border-radius:0 0 10px 10px;overflow:hidden;background:linear-gradient(100deg,#6b5a44 0,#a9855f 30%,#d9b99a 50%,#c79a70 70%,#8b7458 100%);box-shadow:0 4px 8px rgba(0,0,0,.2)}
.search{position:absolute;left:165px;top:217px;width:214px;height:316px;background:rgba(255,255,255,.35);border-radius:6px}
.search-title{position:absolute;left:178px;top:219px;font-family:"Open Sans",sans-serif;font-size:26px;color:#fff;letter-spacing:1.5px}
.select{position:absolute;left:176px;width:188px;height:30px;background:#fff;border-radius:5px;border:1px solid #e2e2e2;font-size:11px;letter-spacing:.6px;color:#666;line-height:28px;padding:0 26px 0 12px;white-space:nowrap;overflow:hidden}
.select::after{content:"";position:absolute;right:8px;top:9px;width:11px;height:11px;border:1px solid #999;background:#eee}
.select::before{content:"";position:absolute;right:11px;top:14px;border:3px solid transparent;border-top:4px solid #444;z-index:1}
.search-btn{position:absolute;left:197px;top:536px;width:140px;height:25px;background:linear-gradient(#5a5a5a,#1f1f1f);border-radius:4px;color:#fff;font-family:"Open Sans",sans-serif;font-size:15px;letter-spacing:1.5px;text-align:center;line-height:25px}
.welcome{position:absolute;left:150px;top:599px;font-family:"Open Sans",sans-serif;font-weight:400;font-size:31px;color:#444}
.welcome b{font-weight:700;color:var(--orange);font-size:24px;margin-left:10px}
.intro{position:absolute;left:155px;top:647px;width:490px;font-size:12px;line-height:22.5px;color:#333}
.intro a{color:var(--orange);text-decoration:none}
.rule{position:absolute;left:150px;width:592px;height:1px;background:#d2cfce}
.list-title{position:absolute;left:151px;top:714px;font-family:"Open Sans",sans-serif;font-weight:400;font-size:20px;color:#444}
.list-title em{color:var(--orange);font-weight:700}
.scrollbar{position:absolute;left:744px;top:712px;width:5px;height:410px;background:#fff}
.scrollbar span{position:absolute;left:0;top:116px;width:5px;height:180px;background:#8d8b8b}
.card{position:absolute;left:0;width:742px;height:180px}
.thumb{position:absolute;left:150px;top:0;width:140px;height:112px;border-radius:4px}
.card--gold .thumb{background:linear-gradient(var(--gold),var(--gold-dark))}
.card--silver .thumb{background:linear-gradient(#eceaea,#c9c6c5)}
.thumb-inner{position:absolute;left:7px;top:7px;width:126px;height:98px;background:#fff;border-radius:4px}
.thumb svg{position:absolute;left:39px;top:25px}
.blurb{position:absolute;left:300px;top:0;width:420px;font-size:12px;line-height:17px;color:#555}
.avatar{position:absolute;left:300px;top:48px;width:72px;height:64px;background:#dcd9d8;border-radius:3px}
.avatar div{position:absolute;left:6px;top:6px;width:60px;height:52px;background:#fff}
.avatar svg{position:absolute;left:22px;top:12px}
.coach{position:absolute;left:380px;top:49px;font-size:12px;line-height:17px;color:#555}
.coach b{color:#444}
.stars{position:absolute;left:385px;top:91px}
.meta{position:absolute;font-size:12px;color:#555}
.meta b{color:#444}
.flag{display:inline-block;width:15px;height:10px;vertical-align:-1px;margin-left:5px;background:linear-gradient(#f39a32 33%,#fff 33% 66%,#2b9a3a 66%)}
.badge{position:absolute;left:151px;top:115px;width:137px;height:27px;background:var(--yellow);border-radius:3px;font-family:"Open Sans",sans-serif;font-style:italic;font-weight:700;font-size:11px;letter-spacing:.6px;color:#222;text-align:center;line-height:27px}
.likes{position:absolute;left:166px;top:148px;font-size:11px;color:#222;display:flex;align-items:center;gap:5px}
.like-btn{display:inline-flex;align-items:center;gap:4px;height:20px;padding:0 6px;border:1px solid #c9cdd6;background:#eef0f5;border-radius:2px;color:#3b5a9a}
.like-btn i{width:8px;height:8px;background:#3b5a9a}
.tags{position:absolute;left:758px;top:608px;width:300px;font-family:"Open Sans",sans-serif;color:var(--tag);line-height:36px;font-size:25px}
.tags .sm{font-size:13px}
.tags .dk{color:var(--tag-strong)}
.tags .lg{font-size:30px}
.footer{position:absolute;left:0;top:1153px;width:1198px;height:47px;background:var(--dark)}
.copyright{position:absolute;left:136px;top:18px;font-size:10.5px;color:#9a9696}
.footer-nav{position:absolute;left:669px;top:19px;display:flex}
.footer-nav a{font-size:10.5px;letter-spacing:1px;color:#9a9696;text-decoration:none;width:82px}
</style>
</head>
<body>
<div class="page">
  <header>
    <div class="header-band"></div>
    <div class="mascot" role="img" aria-label="Caped hero figure illustration"></div>
    <div class="brand">FLIRT NOVA</div>
    <div class="bubble bubble--videos"></div>
    <div class="counter counter--videos">34</div>
    <p class="statement statement--videos">Videos show how to get<br>every woman you want.</p>
    <div class="bubble bubble--coaches"></div>
    <p class="statement statement--coaches">Connect directly with&nbsp;&nbsp;&nbsp;&nbsp;&nbsp;&nbsp;<br>dating-coaches worldwide!</p>
    <div class="counter counter--coaches">26</div>
    <nav class="nav"><a>CONTACT</a><a>ABOUT</a><a>FOLLOW</a><a>SIGN IN</a><a>SIGN UP</a></nav>
  </header>

  <section>
    <div class="hero" role="img" aria-label="Photo of a young couple sharing a strawberry smoothie with two straws"></div>
    <div class="search"></div>
    <div class="search-title">Search</div>
    <div class="select" style="top:257px">Select Language</div>
    <div class="select" style="top:297px">Select Country</div>
    <div class="select" style="top:338px">Select City</div>
    <div class="select" style="top:378px">Select Rating</div>
    <div class="select" style="top:418px">Select Level of Difficulty</div>
    <div class="select" style="top:458px">Select Set-Size</div>
    <div class="select" style="top:497px">-- Conversation Starter --</div>
    <div class="search-btn">Search</div>
  </section>

  <main>
    <h1 class="welcome">Welcome to the <b>FLIRT NOVA</b></h1>
    <p class="intro">Lorem Ipsum is simply dummy text of the printing and typesetting industry. Lorem Ipsum has been the industry's standard dummy texto make a type specimen book. &nbsp;<a>More...</a></p>
    <div class="rule" style="top:705px"></div>
    <h2 class="list-title"><em>TOP 10</em> DATING COACHES listed by best rated videos</h2>
    <div class="scrollbar"><span></span></div>

    <article class="card card--gold" style="top:754px">
      <div class="thumb"><div class="thumb-inner"></div>
        <svg width="46" height="46" viewBox="0 0 46 46"><circle cx="23" cy="23" r="21" fill="#e8eef2" stroke="#b9c0c6" stroke-width="3"/><path d="M17 13 L33 23 L17 33Z" fill="#fff" stroke="#a7b0b7" stroke-width="2"/></svg>
      </div>
      <p class="blurb">Lorem ipsum dolor sit amet consecutor.Lorem ipsum dolor sit amet consecutor.Lorem ipsum dolor sit amet consecutor.Lorem ipsum dolor</p>
      <div class="avatar"><div></div><svg width="28" height="32" viewBox="0 0 28 32"><circle cx="14" cy="9" r="7" fill="#eee" stroke="#aaa"/><path d="M2 31 C2 20 26 20 26 31Z" fill="#eee" stroke="#aaa"/></svg></div>
      <p class="coach"><b>Coach Name</b><br><b>Title of the Video:</b> Lorem ipsum dolor</p>
      <svg class="stars" width="104" height="18" viewBox="0 0 104 18"><g fill="#e0b21a" stroke="#b8890a" stroke-width=".8"><path id="st" d="M9 1l2.4 5.4 5.8.5-4.4 3.9 1.3 5.7L9 13.5 3.9 16.5l1.3-5.7L.8 6.9l5.8-.5Z"/><use href="#st" x="20"/><use href="#st" x="40"/><use href="#st" x="60"/></g><use href="#st" x="80" fill="#f6d24a" stroke="#c99a10"/></svg>
      <p class="meta" style="left:304px;top:131px"><b>Duration :</b> 5 mins</p>
      <p class="meta" style="left:446px;top:131px"><b>Country :</b> India<span class="flag"></span></p>
      <p class="meta" style="left:568px;top:131px"><b>Audio Comment :</b> India</p>
      <p class="meta" style="left:304px;top:154px"><b>Language :</b> English</p>
      <p class="meta" style="left:446px;top:154px"><b>City :</b> New Delhi</p>
      <p class="meta" style="left:568px;top:154px"><b>Difficulty Level :</b> Lorem ipsum</p>
      <div class="badge">TOP DATING COACH</div>
      <div class="likes">1500 <span class="like-btn"><i></i>Like</span></div>
    </article>
    <div class="rule" style="top:929px"></div>

    <article class="card card--silver" style="top:951px">
      <div class="thumb"><div class="thumb-inner"></div>
        <svg width="46" height="46" viewBox="0 0 46 46"><circle cx="23" cy="23" r="21" fill="#e8eef2" stroke="#b9c0c6" stroke-width="3"/><path d="M17 13 L33 23 L17 33Z" fill="#fff" stroke="#a7b0b7" stroke-width="2"/></svg>
      </div>
      <p class="blurb">Lorem ipsum dolor sit amet consecutor.Lorem ipsum dolor sit amet consecutor.Lorem ipsum dolor sit amet consecutor.Lorem ipsum dolor</p>
      <div class="avatar"><div></div><svg width="28" height="32" viewBox="0 0 28 32"><circle cx="14" cy="9" r="7" fill="#eee" stroke="#aaa"/><path d="M2 31 C2 20 26 20 26 31Z" fill="#eee" stroke="#aaa"/></svg></div>
      <p class="coach"><b>Coach Name</b><br><b>Title of the Video:</b> Lorem ipsum dolor</p>
      <svg class="stars" width="104" height="18" viewBox="0 0 104 18"><g fill="#f4c21c" stroke="#c99a10" stroke-width=".8"><path id="st2" d="M9 1l2.4 5.4 5.8.5-4.4 3.9 1.3 5.7L9 13.5 3.9 16.5l1.3-5.7L.8 6.9l5.8-.5Z"/><use href="#st2" x="20"/><use href="#st2" x="40"/><use href="#st2" x="60"/><use href="#st2" x="80"/></g><path d="M89 1v12.5L83.9 16.5l1.3-5.7-4.4-3.9 5.8-.5Z" fill="#8a6a10" opacity=".5"/></svg>
      <p class="meta" style="left:304px;top:131px"><b>Duration :</b> 5 mins</p>
      <p class="meta" style="left:446px;top:131px"><b>Country :</b> India<span class="flag"></span></p>
      <p class="meta" style="left:568px;top:131px"><b>Audio Comment :</b> India</p>
      <p class="meta" style="left:304px;top:154px"><b>Language :</b> English</p>
      <p class="meta" style="left:446px;top:154px"><b>City :</b> New Delhi</p>
      <p class="meta" style="left:568px;top:154px"><b>Difficulty Level :</b> Lorem ipsum</p>
    </article>

    <aside class="tags">bitch shield, blow out<br>opener, <span class="sm">bounce</span>,<br><span class="dk lg">calibration</span>, canned<br>routine, <span class="sm">challenge point</span>, cock-<br>block, <span class="dk">cold approach</span>, <span class="sm">cold</span><br><span class="sm">reading</span>, compliment opener</aside>
  </main>

  <footer class="footer">
    <p class="copyright">Copyright © 2012 FlirtNova. All Rights Reserved.</p>
    <nav class="footer-nav"><a>CONTACT</a><a>ABOUT</a><a>FOLLOW</a><a>SIGN IN</a><a>SIGN UP</a></nav>
  </footer>
</div>
</body>
</html>
```